Photojournalism/photography business needs a simple, timeless & professional letterhead design

We need a letterhead design for photography/photojournalism business called 'plomk', no capitals.

The letterhead needs to be:
- simple
- professional
- timeless
- easy to read
- consists of at least 2 colors to make it stands out.

We do mainly editorial photography, photo articles for various publications, travel, businesses, as well as people such as family and kids.

The final design should communicate professionalism, easy identification, attention grabbing, even if it has to be found among a stack of various papers on the clients' desks.

Target Market(s)

Various publications.

Industry/Entity Type

Business

Requirements
Must have
• Please use the logo attached.

```html
<!DOCTYPE html>
<html lang="en">
<head>
<meta charset="utf-8">
<title>plomk — stationery</title>
<link href="https://fonts.googleapis.com/css2?family=Alegreya+Sans:wght@700;800&display=swap" rel="stylesheet">
<style>
  :root {
    --backdrop: #fbc982;
    --brand-blue: #00b8f1;
    --brand-blue-deep: #009fd3;
    --ink: #3a3a3a;
    --paper: #ffffff;
    --paper-shade: #ececec;
    --contact-text: #ffffff;
  }
  * { margin: 0; padding: 0; box-sizing: border-box; }
  html, body { width: 1200px; height: 1000px; overflow: hidden; }
  body {
    position: relative;
    background: var(--backdrop);
    font-family: "Alegreya Sans", sans-serif;
  }
  .sheet {
    position: absolute;
    overflow: hidden;
  }
  .sheet--cover {
    left: 195px; top: 199px; width: 337px; height: 477px;
    background:
      radial-gradient(circle at 0 0, var(--brand-blue-deep) 0, rgba(0,159,211,0) 110px),
      var(--brand-blue);
  }
  .sheet--letter {
    left: 667px; top: 200px; width: 342px; height: 479px;
    background:
      radial-gradient(circle at 0 0, var(--paper-shade) 0, rgba(236,236,236,0) 130px),
      var(--paper);
    border-radius: 2px;
  }
  .wordmark {
    position: absolute;
    font-weight: 800;
    color: var(--ink);
    letter-spacing: -0.5px;
    line-height: 1;
  }
  .sheet--cover .wordmark { left: 122px; top: 192px; font-size: 34px; }
  .sheet--letter .wordmark { left: 62px; top: 40px; font-size: 28px; }
  .contact-block {
    position: absolute;
    left: 176px; top: 358px; width: 145px; height: 82px;
  }
  .contact-block svg { position: absolute; left: 0; top: 0; }
  .contact-lines {
    position: absolute;
    right: 17px; top: 26px;
    text-align: right;
    color: var(--contact-text);
    font-weight: 700;
    font-size: 6.4px;
    line-height: 8.6px;
    list-style: none;
  }
</style>
</head>
<body>
  <section class="sheet sheet--cover" aria-label="Folder cover">
    <span class="wordmark">plomk</span>
  </section>

  <section class="sheet sheet--letter" aria-label="Letterhead">
    <span class="wordmark">plomk</span>
    <div class="contact-block">
      <svg width="145" height="82" viewBox="0 0 145 82" aria-hidden="true">
        <defs>
          <linearGradient id="block-shadow" x1="0" y1="0" x2="0" y2="1">
            <stop offset="0" stop-color="#000" stop-opacity="0.12"/>
            <stop offset="1" stop-color="#000" stop-opacity="0"/>
          </linearGradient>
        </defs>
        <rect x="16" y="70" width="122" height="6" fill="url(#block-shadow)"/>
        <line x1="5" y1="74" x2="74" y2="5" stroke="#3a3a3a" stroke-width="1.4"/>
        <polygon points="41,24 136,24 136,69 20,69" fill="#00b8f1"/>
      </svg>
      <ul class="contact-lines">
        <li>+001 555 0142</li>
        <li>www.plomk.com</li>
        <li>info@plomk.com</li>
        <li>12 Harbor Lane, Easton 000451</li>
      </ul>
    </div>
  </section>
</body>
</html>
```